Personnel Safety & Tracking Systems by velqor

Create a sales presentation to communicate how velqor can help prospective clients in mining and tunnelling to implement IoT systems and create smart sites which can -

Identify, monitor & locate assets;
- personnel
- equipment
- vehicles

Chapters to include:
- about / why us
- how does it work
- system architecture
- features & benefits
- software & hardware specs
- case studies (see attached)
- testimonials
- pricing

1. Learn more about velqor systems at below link
https://velqor.example/crew-location-for-safety/

2. See uploaded existing presentation docs / case studies -

Note: We are looking for a corporate presentation which communicates clearly what velqor can offer. The system has many facets to incorporate, the key to good design communication will be simplifying what can appear to be a technical topic, deliver a simple product and comprehensive solution.

We require more than a template design, the designer must understand and clearly illustrate the product, new graphics will be required. We are available for guidance and can provide any text/content you require.

Competitors:
https://brindlepath.example (this is the most relevant)
https://www.mavolinkworks.example/shift-buddy-for-safe-mining (this will help you learn about the solution)

Note: The competitor products are rather less versatile and advanced than velqor system, we can provide further briefing, as required.

Target Market(s)

Staff safety and project management teams working for mining and tunnelling companies

Industry/Entity Type

Mining and Tunneling

Requirements
Must have
• System architectural diagrams and illustrations, infographics and visualisation to help communicate - system, features and benefits. Also hardware and software specifications for complete picture of the product.

```html
<!DOCTYPE html>
<html lang="en">
<head>
<meta charset="utf-8">
<title>Velqor Smart Site – Personnel Safety &amp; Tracking</title>
<link rel="stylesheet" href="https://fonts.googleapis.com/css2?family=Montserrat:wght@600;700&family=Inter:wght@400;500&display=swap">
<style>
  :root {
    --page-bg: #ececec;
    --navy-deep: #121a3b;
    --navy: #1a2450;
    --navy-soft: #243166;
    --line: rgba(120, 150, 220, 0.35);
    --bar: #3f5a9c;
    --bar-text: #dbe6ff;
    --text: #c9d4f2;
    --text-dim: #8393bf;
    --accent-orange: #f59a2e;
    --accent-purple: #7d4fd6;
    --icon-ring: #4c66a8;
  }
  * { box-sizing: border-box; margin: 0; padding: 0; }
  html, body { width: 1200px; height: 788px; overflow: hidden; }
  body { background: var(--page-bg); font-family: "Inter", sans-serif; position: relative; }
  .slide {
    position: absolute; left: 250px; top: 44px;
    width: 700px; height: 700px;
    background: linear-gradient(180deg, var(--navy-deep) 0%, var(--navy) 55%, var(--navy-deep) 100%);
    overflow: hidden;
  }
  .slide-frame { position: absolute; inset: 22px; border: 1px solid var(--line); pointer-events: none; }
  .hero-scene {
    position: absolute; left: 0; top: 0; width: 700px; height: 300px;
    background:
      radial-gradient(ellipse 150px 60px at 300px 215px, rgba(245,154,46,0.75), transparent 70%),
      radial-gradient(ellipse 120px 80px at 190px 150px, rgba(245,120,90,0.6), transparent 70%),
      radial-gradient(ellipse 300px 130px at 230px 140px, rgba(125,79,214,0.6), transparent 75%),
      linear-gradient(180deg, var(--navy-deep) 0%, #262a66 35%, #1e2758 70%, var(--navy) 100%);
  }
  .connectors { position: absolute; left: 0; top: 0; }
  .bar {
    position: absolute; height: 24px; border-radius: 4px;
    background: var(--bar); color: var(--bar-text);
    font-family: "Montserrat", sans-serif; font-weight: 600; font-size: 12px;
    line-height: 24px; padding: 0 12px; letter-spacing: 0.02em; white-space: nowrap;
  }
  .title-bar { left: 90px; top: 58px; width: 210px; font-weight: 700; }
  .assets-bar { left: 340px; top: 304px; width: 170px; }
  .how-bar { left: 70px; top: 410px; width: 220px; }
  .step-list { position: absolute; left: 70px; top: 452px; list-style: none; }
  .step { display: flex; align-items: center; gap: 12px; height: 50px; }
  .step-icon {
    width: 30px; height: 30px; border-radius: 50%;
    border: 1.5px solid var(--icon-ring); background: var(--navy-soft);
    display: flex; align-items: center; justify-content: center; flex: none;
  }
  .step-title { font-family: "Montserrat", sans-serif; font-size: 10px; font-weight: 600; color: var(--bar-text); }
  .step-text { font-size: 9px; color: var(--text-dim); margin-top: 2px; }
  .asset-columns { position: absolute; left: 340px; top: 342px; display: flex; gap: 14px; }
  .asset { width: 96px; }
  .asset-title {
    font-family: "Montserrat", sans-serif; font-size: 10px; font-weight: 600;
    color: var(--bar-text); display: flex; align-items: center; gap: 6px;
  }
  .asset-title::before { content: ""; width: 5px; height: 5px; border-radius: 50%; background: var(--accent-orange); }
  .asset-text { font-size: 9px; line-height: 1.4; color: var(--text-dim); margin-top: 4px; }
  .benefit-panel {
    position: absolute; left: 380px; top: 440px; width: 290px; height: 200px;
    border: 1px solid var(--line); border-radius: 6px;
  }
  .benefit-panel .bar { right: 16px; top: 16px; }
  .benefit-icon {
    position: absolute; left: 22px; top: 84px; width: 38px; height: 38px; border-radius: 50%;
    background: radial-gradient(circle, var(--accent-orange) 0%, #b0521f 70%);
  }
  .benefit-copy { position: absolute; left: 76px; top: 82px; width: 190px; }
  .benefit-title { font-family: "Montserrat", sans-serif; font-size: 11px; font-weight: 600; color: var(--bar-text); }
  .benefit-text { font-size: 9px; line-height: 1.5; color: var(--text); margin-top: 4px; }
</style>
</head>
<body>
  <main class="slide">
    <div class="hero-scene" role="img" aria-label="Illustration: orange mining vehicles on a night-time mountain site under a purple and orange glow"></div>

    <svg class="connectors" width="700" height="700" viewBox="0 0 700 700" aria-hidden="true">
      <g fill="none" stroke="rgba(140,170,235,0.45)" stroke-width="1">
        <path d="M195 82 V120 H300 V200"/>
        <path d="M560 86 V120 H400 V185"/>
        <path d="M70 240 H150 V215"/>
        <path d="M630 230 H520 V205"/>
      </g>
      <g fill="#243166" stroke="#6a86c8" stroke-width="1.5">
        <circle cx="300" cy="206" r="7"/>
        <circle cx="400" cy="191" r="7"/>
        <circle cx="150" cy="209" r="7"/>
        <circle cx="520" cy="199" r="7"/>
      </g>
      <g fill="#dbe6ff">
        <circle cx="300" cy="206" r="2.5"/>
        <circle cx="400" cy="191" r="2.5"/>
        <circle cx="150" cy="209" r="2.5"/>
        <circle cx="520" cy="199" r="2.5"/>
      </g>
      <polygon points="560,62 570,68 570,80 560,86 550,80 550,68" fill="#f59a2e"/>
    </svg>

    <div class="slide-frame"></div>

    <div class="bar title-bar">Velqor Smart Site</div>
    <div class="bar assets-bar">Assets Tracked</div>
    <div class="bar how-bar">How It Works</div>

    <section class="asset-columns">
      <div class="asset"><p class="asset-title">Personnel</p><p class="asset-text">Real-time crew location and headcount</p></div>
      <div class="asset"><p class="asset-title">Equipment</p><p class="asset-text">Monitor usage and maintenance status</p></div>
      <div class="asset"><p class="asset-title">Vehicles</p><p class="asset-text">Collision avoidance and route tracking</p></div>
    </section>

    <ul class="step-list">
      <li class="step">
        <span class="step-icon"><svg width="14" height="14" viewBox="0 0 14 14"><circle cx="7" cy="4.5" r="2.5" fill="none" stroke="#c9d4f2" stroke-width="1.3"/><path d="M2.5 13c0-3 2-4.5 4.5-4.5s4.5 1.5 4.5 4.5" fill="none" stroke="#c9d4f2" stroke-width="1.3"/></svg></span>
        <div><p class="step-title">Tag Wearables</p><p class="step-text">Worn by every crew member</p></div>
      </li>
      <li class="step">
        <span class="step-icon"><svg width="14" height="14" viewBox="0 0 14 14"><path d="M3 9a5 5 0 0 1 8 0M5 11a2.5 2.5 0 0 1 4 0" fill="none" stroke="#c9d4f2" stroke-width="1.3"/><circle cx="7" cy="12.5" r="1" fill="#c9d4f2"/></svg></span>
        <div><p class="step-title">Gateways</p><p class="step-text">Mesh network underground</p></div>
      </li>
      <li class="step">
        <span class="step-icon"><svg width="14" height="14" viewBox="0 0 14 14"><path d="M4 11h7a3 3 0 0 0 0-6 4 4 0 0 0-7.5 1A2.5 2.5 0 0 0 4 11z" fill="none" stroke="#c9d4f2" stroke-width="1.3"/></svg></span>
        <div><p class="step-title">Cloud Platform</p><p class="step-text">Live location dashboard</p></div>
      </li>
      <li class="step">
        <span class="step-icon"><svg width="14" height="14" viewBox="0 0 14 14"><path d="M7 1.5 13 12.5H1z" fill="none" stroke="#f59a2e" stroke-width="1.3"/><path d="M7 5.5v3.5" stroke="#f59a2e" stroke-width="1.3"/></svg></span>
        <div><p class="step-title">Alerts</p><p class="step-text">Instant safety notifications</p></div>
      </li>
    </ul>

    <section class="benefit-panel">
      <div class="bar">Key Benefit</div>
      <span class="benefit-icon"></span>
      <div class="benefit-copy">
        <p class="benefit-title">Safer Sites</p>
        <p class="benefit-text">Faster emergency response with every worker located in seconds.</p>
      </div>
    </section>
  </main>
</body>
</html>
```